Business Card for Sugared Soiree

I have a logo for my candy buffet business, and need a business card designed using that logo. Sugared Soiree designs and builds beautiful and delicious candy and dessert tables for all kinds of events. The card should be simple, modern, graphic, colorful, and use the Sugared Soiree Logo.

Target Market(s)

The target market is people hosting major parties and events. This includes brides getting married, parents hosting birthday parties/Sweet Sixteen/Bar Mitzvah/quinceanera parties, and companies hosting corporate events.

Industry/Entity Type

Business

Requirements
Must have
• The business card must have the logo, with or without the tag line.

The following information must be on the card:

Dana Whitfield
CEO & Candy Stylist
614.392.5071
dana@sugaredsoiree-example.com
Nice to have
• I like the idea of having multiple colors of the same design so that several people receiving cards will each receive a different color. Perhaps 3-5 colors or variations on a basic card design.

```html
<!DOCTYPE html>
<html lang="en">
<head>
<meta charset="utf-8">
<title>Sugared Soiree – Business Card</title>
<link rel="stylesheet" href="https://fonts.googleapis.com/css2?family=Questrial&family=Didact+Gothic&display=swap">
<style>
  :root {
    --stage: #2b2b2d;
    --candy-pink: #e8199a;
    --candy-pink-light: #ef5db8;
    --blush: #f28fcb;
    --paper: #f7f7f7;
    --ink: #1c1c1c;
    --ink-soft: #4a4a4a;
    --white: #ffffff;
  }
  * { box-sizing: border-box; margin: 0; padding: 0; }
  html, body {
    width: 1200px; height: 1024px; overflow: hidden;
    background: var(--stage);
  }
  .canvas {
    position: relative; width: 1200px; height: 1024px;
    display: flex; flex-direction: column; align-items: center; justify-content: center;
    gap: 40px;
  }
  .card {
    position: relative; width: 820px; height: 468px;
    border-radius: 4px; overflow: hidden;
    box-shadow: 0 18px 40px rgba(0,0,0,.45);
  }

  /* Front */
  .card--front {
    background: linear-gradient(135deg, var(--candy-pink-light) 0%, var(--candy-pink) 55%, #d4108a 100%);
    color: var(--white);
    display: flex; flex-direction: column; align-items: center; justify-content: center;
    font-family: "Questrial", sans-serif;
  }
  .front__brand { display: flex; align-items: center; gap: 22px; }
  .brand-dot {
    flex: none; width: 46px; height: 46px; border-radius: 50%;
    background: var(--white);
  }
  .front__wordmark { font-size: 72px; letter-spacing: 1px; line-height: 1; }
  .front__tagline {
    display: flex; align-items: center; gap: 16px;
    margin-top: 16px; width: 580px;
    font-size: 16px; white-space: nowrap;
  }
  .front__tagline::before, .front__tagline::after {
    content: ""; flex: 1; height: 2px; background: rgba(255,255,255,.85);
  }
  .front__web { margin-top: 34px; font-size: 21px; letter-spacing: .5px; }

  /* Back */
  .card--back {
    background: linear-gradient(160deg, var(--white) 0%, var(--paper) 70%, #ececec 100%);
    color: var(--ink);
    font-family: "Questrial", sans-serif;
  }
  .back__brand {
    position: absolute; right: 56px; top: 64px;
    display: flex; align-items: center; gap: 18px;
  }
  .back__brand .brand-dot { width: 38px; height: 38px; background: var(--candy-pink); }
  .back__wordmark { font-size: 58px; line-height: 1; color: var(--ink); }
  .back__person { position: absolute; right: 56px; top: 168px; text-align: right; }
  .back__name { font-size: 30px; line-height: 1.1; }
  .back__name .first { color: var(--candy-pink); }
  .back__name .last { color: var(--blush); }
  .back__role {
    margin-top: 6px; font-size: 20px; font-style: italic; color: var(--ink-soft);
    font-family: "Didact Gothic", sans-serif;
  }
  .contact {
    position: absolute; display: flex; align-items: center; gap: 14px;
    font-size: 21px; color: var(--ink-soft); white-space: nowrap;
  }
  .contact--phone { left: 44px; top: 300px; }
  .contact--email { right: 56px; bottom: 52px; }
  .contact__icon {
    flex: none; width: 30px; height: 30px; border-radius: 50%;
    background: var(--blush);
    display: flex; align-items: center; justify-content: center;
  }
</style>
</head>
<body>
<main class="canvas">

  <section class="card card--front" aria-label="Card front">
    <div class="front__brand">
      <span class="brand-dot"></span>
      <span class="front__wordmark">sugaredsoiree</span>
    </div>
    <p class="front__tagline">sweet tables for every event</p>
    <p class="front__web">www.sugaredsoiree-example.com</p>
  </section>

  <section class="card card--back" aria-label="Card back">
    <div class="back__brand">
      <span class="brand-dot"></span>
      <span class="back__wordmark">sugaredsoiree</span>
    </div>
    <div class="back__person">
      <p class="back__name"><span class="first">dana</span><span class="last">whitfield</span></p>
      <p class="back__role">ceo &amp; candy stylist</p>
    </div>
    <p class="contact contact--phone">
      <span class="contact__icon">
        <svg width="16" height="16" viewBox="0 0 24 24" aria-hidden="true">
          <path fill="#fff" d="M6.6 10.8a15.2 15.2 0 0 0 6.6 6.6l2.2-2.2a1 1 0 0 1 1-.25 11.4 11.4 0 0 0 3.6.57 1 1 0 0 1 1 1V20a1 1 0 0 1-1 1A17 17 0 0 1 3 4a1 1 0 0 1 1-1h3.5a1 1 0 0 1 1 1c0 1.25.2 2.45.57 3.57a1 1 0 0 1-.25 1z"/>
        </svg>
      </span>
      614.392.5071
    </p>
    <p class="contact contact--email">
      <span class="contact__icon">
        <svg width="16" height="16" viewBox="0 0 24 24" aria-hidden="true">
          <rect x="3" y="6" width="18" height="12" rx="1.5" fill="#fff"/>
          <path d="M3.5 7l8.5 6 8.5-6" fill="none" stroke="#f28fcb" stroke-width="1.6"/>
        </svg>
      </span>
      dana@sugaredsoiree-example.com
    </p>
  </section>

</main>
</body>
</html>
```